Looking for a modern elegant home improvment website

Looking for a new Design on current website . Please us www.larkfieldbuilders.example PIctures of recent work and stock photos that were attached , Free estimates , Explaining what we do , Similiar to www. larkfieldbuilders.example which is our current webpage . Colors can be different . I have attached our buisness card as well as our postcard we send out to homes . I would like a modern web page that our costumers can feel is professional so they can have a feeling of trust when they hire us . Our address should be on there . Licenesed & Insured should be somewhere on the page . Our Company Logo should be there as well . It would be nice to have a very modern website with great pictures of home interiors and exteriors . a page describing what we do is very important . facebook link to our page is a must as well as a instagram .
Updates

Reason: Looking for a elegant modern 5 page website with proper spelling and professional looking . I extended the deadline and upgraded .

Reason: Looking for more design options .

Target Market(s)

Home owners , Commerical buisness,

Industry/Entity Type

Home Improvement

Number of Pages Required

5+ page

Font styles to use
Serif

Requirements
Must have
• PIctures of recent work and stock photos that were attached , Free estimates , Explaining what we do , Similiar to www. larkfieldbuilders.example which is our current webpage . Colors can be different . I have attached our buisness card as well as our postcard we send out to homes . I would like a modern web page that our costumers can feel is professional so they can have a feeling of trust when they hire us . Our address should be on there . Licenesed & Insured should be somewhere on the page . Our Company Logo should be there as well .
Nice to have
• It would be nice to have a very modern website with great pictures of home interiors and exteriors . a page describing what we do is very important . facebook link to our page is a must as well as a instagram .

```html
<!DOCTYPE html>
<html lang="en">
<head>
<meta charset="utf-8">
<title>Larkfield Builders LLC — Home Improvement</title>
<link href="https://fonts.googleapis.com/css2?family=Open+Sans:wght@400;600;700&display=swap" rel="stylesheet">
<style>
:root{
  --navy:#1f3a64;
  --navy-deep:#1a3358;
  --blue:#1f78c1;
  --sky:#2f8fd6;
  --ink:#2b2b2b;
  --muted:#777;
  --line:#d9d9d9;
  --paper:#ffffff;
  --mist:#eceef1;
  --accent:#e58a2a;
}
*{box-sizing:border-box;margin:0;padding:0}
html,body{width:1200px;height:3084px;overflow:hidden}
body{font-family:"Open Sans",Arial,sans-serif;color:var(--ink);background:var(--paper);position:relative}
.abs{position:absolute}
svg{display:block}

/* header */
.site-header{left:0;top:0;width:1200px;height:120px;background:var(--paper)}
.brand{left:150px;top:34px;display:flex;align-items:center;gap:12px}
.brand-mark{width:22px;height:22px;background:var(--navy)}
.brand-name{font-size:19px;font-weight:700;color:var(--navy)}
.topbar{right:150px;top:16px;display:flex;align-items:center;gap:10px;font-size:15px;font-weight:600;color:var(--navy)}
.topbar .dot{width:22px;height:22px;border-radius:50%;background:var(--navy)}
.topbar svg{width:16px;height:16px}
.main-nav{left:470px;top:58px;display:flex;font-size:14px;color:var(--navy)}
.main-nav a{display:block;padding:0 18px;line-height:46px;text-decoration:none;color:inherit}
.main-nav a.active{background:var(--navy);color:#fff}
.btn-estimate{left:910px;top:62px;width:140px;height:36px;border-radius:18px;background:var(--blue);color:#fff;font-size:14px;font-weight:600;text-align:center;line-height:36px}

/* hero */
.hero{left:0;top:120px;width:1200px;height:392px;background:linear-gradient(135deg,#8a6a4c 0%,#c9b39a 40%,#6e5440 75%,#3e3128 100%)}
.hero-shade{left:0;top:120px;width:1200px;height:392px;background:rgba(20,28,40,.35)}
.hero-copy{left:0;top:180px;width:1200px;text-align:center;color:#fff}
.hero-copy .kicker{font-size:20px;font-weight:600}
.hero-copy h1{font-size:58px;font-weight:700;line-height:1.1;margin-top:4px}
.hero-copy .sub{font-size:22px;margin-top:2px}
.btn-ghost{display:inline-block;margin-top:22px;padding:8px 22px;border:1px solid #fff;border-radius:16px;font-size:14px}
.hero-arrow{top:280px;width:30px;height:30px}

/* services */
.service{top:520px;width:272px}
.service .photo{height:192px}
.service h3{font-size:22px;font-weight:600;color:var(--accent);margin-top:20px;line-height:30px}
.service p{font-size:14px;line-height:20px;height:60px;overflow:hidden;color:var(--muted);margin-top:4px}
.btn-outline{display:inline-block;margin-top:16px;padding:6px 18px;border:1px solid #999;border-radius:16px;font-size:13px;color:var(--ink)}
.btn-solid{display:inline-block;margin-top:16px;padding:7px 18px;border-radius:16px;font-size:13px;color:#fff;background:var(--navy)}
.service-bar{left:0;top:918px;width:1200px;height:4px;background:var(--navy)}
.service-bar i{position:absolute;left:440px;top:-2px;width:320px;height:8px;background:var(--sky)}

/* about */
.about{left:0;top:940px;width:1200px;height:440px;background:var(--navy)}
.about-photo{left:160px;top:1025px;width:280px;height:280px;border-radius:50%;border:10px solid var(--sky);background:linear-gradient(135deg,#c79a66,#7a5634 60%,#3d2b1c)}
.about-copy{left:520px;top:1015px;width:520px;color:#fff}
.about-copy h2{font-size:36px;font-weight:600}
.about-copy .sub{font-size:17px;margin-top:2px}
.about-copy p{font-size:14px;line-height:1.5;margin-top:22px;color:#dbe4f0}
.about-copy .btn-ghost{margin-top:32px}

/* work */
.section-title{left:0;width:1200px;text-align:center}
.section-title h2{font-size:38px;font-weight:600;color:var(--navy);line-height:52px}
.section-title p{font-size:17px;color:var(--muted);margin-top:2px}
.tile{overflow:hidden}
.tile-overlay{left:0;top:0;width:100%;height:100%;background:rgba(31,58,100,.75);color:#fff;text-align:center;padding-top:96px;font-size:15px}
.tile-overlay span{display:inline-block;margin-top:14px;padding:5px 14px;border:1px solid #fff;border-radius:14px;font-size:13px}

/* testimonials */
.testi-photo{left:560px;top:2140px;width:80px;height:80px;border-radius:50%;background:linear-gradient(160deg,#dfe6ee,#9eb1c6);border:4px solid #fff;box-shadow:0 0 0 2px var(--line)}
.testi-dots{left:612px;top:2196px;display:flex;gap:4px}
.testi-dots i{width:14px;height:14px;border-radius:50%;background:var(--sky)}
.testi-copy{left:0;top:2256px;width:1200px;text-align:center}
.testi-copy q{font-size:14px;color:var(--muted)}
.testi-copy h4{font-size:22px;font-weight:600;color:var(--accent);margin-top:18px}
.testi-copy .place{font-size:14px;color:var(--muted)}
.testi-arrow{top:2176px;width:30px;height:30px}

/* cta */
.cta{left:0;top:2416px;width:1200px;height:112px;background:linear-gradient(90deg,var(--navy-deep) 0%,var(--navy) 55%,var(--sky) 100%)}
.cta-copy{left:150px;top:2448px;color:#fff}
.cta-copy h3{font-size:18px;font-weight:600}
.cta-copy p{font-size:13px;color:#cdd9ea;margin-top:2px}
.btn-cta{left:910px;top:2452px;padding:7px 26px;border:1px solid #fff;border-radius:16px;font-size:14px;color:#fff}

/* contact */
.contact{left:0;top:2528px;width:1200px;height:412px;background:var(--mist)}
.form{left:150px;top:2570px;width:360px}
.form h3,.info h3{font-size:20px;font-weight:600;color:var(--ink);margin-bottom:22px}
.field{height:32px;background:#fff;border:1px solid var(--line);margin-bottom:12px;font-size:12px;color:#999;padding:7px 10px}
.field.tall{height:78px}
.btn-send{display:inline-block;padding:6px 20px;background:var(--navy);color:#fff;font-size:13px;border-radius:14px;margin-top:6px}
.divider{left:600px;top:2570px;width:1px;height:330px;background:var(--line)}
.info{left:680px;top:2570px;width:380px}
.info-row{display:flex;gap:20px;margin-bottom:18px;font-size:12px;line-height:1.45;color:#555}
.info-row svg{width:18px;height:18px;flex:none;margin-top:2px}
.info-row b{display:block;font-weight:600;color:var(--ink)}
.follow{display:flex;align-items:center;gap:10px;font-size:13px;color:#555;margin-top:20px}
.follow i{width:22px;height:22px;border-radius:50%;background:var(--navy)}

/* footer */
.footer-top{left:590px;top:2928px;width:22px;height:22px;border-radius:50%;border:1px solid var(--line);background:var(--paper)}
.footer-nav{left:0;top:3004px;width:1200px;display:flex;justify-content:center;gap:40px;font-size:14px;color:var(--navy)}
.copyright{left:0;top:3044px;width:1200px;text-align:center;font-size:12px;color:var(--muted)}
.footer-line{left:150px;top:2990px;width:900px;height:1px;background:var(--line)}
</style>
</head>
<body>

<header class="abs site-header">
  <div class="abs brand"><span class="brand-mark"></span><span class="brand-name">Larkfield Builders LLC</span></div>
  <div class="abs topbar">
    <span>Call Us</span>
    <svg viewBox="0 0 24 24"><path fill="#1f3a64" d="M6.6 10.8a15 15 0 0 0 6.6 6.6l2.2-2.2a1 1 0 0 1 1-.25 11.4 11.4 0 0 0 3.6.57 1 1 0 0 1 1 1V20a1 1 0 0 1-1 1A17 17 0 0 1 3 4a1 1 0 0 1 1-1h3.5a1 1 0 0 1 1 1c0 1.25.2 2.45.57 3.6a1 1 0 0 1-.25 1z"/></svg>
    <span>201-555-0148</span>
    <span class="dot"></span><span class="dot"></span><span class="dot"></span>
  </div>
  <nav class="abs main-nav">
    <a class="active" href="#">Home</a><a href="#">About Us</a><a href="#">Services</a><a href="#">Gallery</a><a href="#">Contact Us</a>
  </nav>
  <div class="abs btn-estimate">Free Estimate</div>
</header>

<div class="abs hero" role="img" aria-label="Photo of a remodelled kitchen with wood cabinets and marble counters"></div>
<div class="abs hero-shade"></div>
<svg class="abs hero-arrow" style="left:230px" viewBox="0 0 30 30"><path d="M19 6 10 15l9 9" fill="none" stroke="#fff" stroke-width="2"/></svg>
<svg class="abs hero-arrow" style="left:940px" viewBox="0 0 30 30"><path d="m11 6 9 9-9 9" fill="none" stroke="#fff" stroke-width="2"/></svg>
<div class="abs hero-copy">
  <div class="kicker">We are tile &amp; marble specialist</div>
  <h1>We Build</h1>
  <div class="sub">bathrooms · kitchens · Additions and much more</div>
  <span class="btn-ghost">Explore More</span>
</div>

<section class="services">
  <article class="abs service" style="left:150px">
    <div class="photo" role="img" aria-label="Photo of new hardwood flooring" style="background:linear-gradient(135deg,#b98552,#7a4f2a 60%,#d7b48a)"></div>
    <h3>Flooring</h3>
    <p>We install hardwood, tile and stone floors built to last, with careful prep and a clean finish in every room.</p>
    <span class="btn-outline">Read More</span>
  </article>
  <article class="abs service" style="left:464px">
    <div class="photo" role="img" aria-label="Photo of a bright room with new windows and doors" style="background:linear-gradient(135deg,#e9dcc6,#b99a72 55%,#6f5438)"></div>
    <h3>Windows and Doors</h3>
    <p>Energy efficient windows and sturdy entry doors, measured and fitted by our crew for comfort and light.</p>
    <span class="btn-solid">Read More</span>
  </article>
  <article class="abs service" style="left:778px">
    <div class="photo" role="img" aria-label="Photo of a remodelled kitchen with an island" style="background:linear-gradient(135deg,#d8a066,#8c5a2e 55%,#f0dcc0)"></div>
    <h3>Kitchens and Bathrooms</h3>
    <p>Full kitchen and bath remodels, from custom tile and marble work to cabinets, counters and fixtures.</p>
    <span class="btn-outline">Read More</span>
  </article>
  <div class="abs service-bar"><i></i></div>
</section>

<section class="about-section">
  <div class="abs about"></div>
  <div class="abs about-photo" role="img" aria-label="Photo of a finished kitchen interior"></div>
  <div class="abs about-copy">
    <h2>About Us</h2>
    <div class="sub">Licensed &amp; Fully Insured</div>
    <p>Your home is the most important asset you have, so when you are ready to build or remodel, put yourself in the hands of a trusted general contractor. We have been building for over 20 years, specializing in residential construction. We are tile &amp; marble specialists. We build bathrooms, kitchens, additions and much more. Give us a try, we do great work and are very passionate about what we do. We are a family owned business that has been in the construction field for over 20 years.</p>
    <span class="btn-ghost">Discover More</span>
  </div>
</section>

<section class="latest-work">
  <div class="abs section-title" style="top:1424px">
    <h2>Our Latest Work</h2>
    <p>Check out a few of our completed projects !</p>
  </div>
  <div class="abs tile" style="left:0;top:1512px;width:300px;height:248px;background:linear-gradient(135deg,#d9d4cc,#9a948a)" role="img" aria-label="Photo of a freshly built wooden deck"></div>
  <div class="abs tile" style="left:300px;top:1512px;width:300px;height:248px;background:#5a4a3a" role="img" aria-label="Photo of an interior design project">
    <div class="abs tile-overlay">Interior Design Ideas<br><span>View Project</span></div>
  </div>
  <div class="abs tile" style="left:600px;top:1512px;width:300px;height:248px;background:linear-gradient(135deg,#3e3a36,#8a7a66)" role="img" aria-label="Photo of a tiled floor with dark trim"></div>
  <div class="abs tile" style="left:900px;top:1512px;width:300px;height:248px;background:linear-gradient(135deg,#f0ece6,#c2b8aa)" role="img" aria-label="Photo of a white kitchen"></div>
  <div class="abs tile" style="left:0;top:1760px;width:300px;height:240px;background:linear-gradient(135deg,#c3bfb8,#7e7a72)" role="img" aria-label="Photo of a deck with white railings"></div>
  <div class="abs tile" style="left:300px;top:1760px;width:300px;height:240px;background:linear-gradient(135deg,#7a4a2c,#c68a52)" role="img" aria-label="Photo of wood plank flooring"></div>
  <div class="abs tile" style="left:600px;top:1760px;width:300px;height:240px;background:linear-gradient(135deg,#b89a7a,#5b4532)" role="img" aria-label="Photo of a remodelled room with wood floors"></div>
  <div class="abs tile" style="left:900px;top:1760px;width:300px;height:240px;background:linear-gradient(135deg,#4a3a2c,#a48868)" role="img" aria-label="Photo of a kitchen sink and cabinets"></div>
</section>

<section class="testimonials">
  <div class="abs section-title" style="top:2050px">
    <h2>Testimonials</h2>
    <p>We always listen to our clients</p>
  </div>
  <div class="abs testi-photo" role="img" aria-label="Portrait of a client"></div>
  <div class="abs testi-dots"><i></i><i></i><i></i></div>
  <svg class="abs testi-arrow" style="left:230px" viewBox="0 0 30 30"><path d="M19 6 10 15l9 9" fill="none" stroke="#c9d4e2" stroke-width="2"/></svg>
  <svg class="abs testi-arrow" style="left:940px" viewBox="0 0 30 30"><path d="m11 6 9 9-9 9" fill="none" stroke="#2f8fd6" stroke-width="2"/></svg>
  <div class="abs testi-copy">
    <q>Trusted crew, reliable, very professional about what they do. Thanks for a job well done</q>
    <h4>Dana Whitfield</h4>
    <div class="place">Ridgeview, NJ</div>
  </div>
</section>

<section class="call-to-action">
  <div class="abs cta"></div>
  <div class="abs cta-copy">
    <h3>Our Team of Experts will make your Dreams</h3>
    <p>into creative construction jobs, from planning your ideas to building your dream home</p>
  </div>
  <div class="abs btn-cta">Contact Us</div>
</section>

<section class="contact-section">
  <div class="abs contact"></div>
  <div class="abs form">
    <h3>Get in Touch</h3>
    <div class="field">Name</div>
    <div class="field">Phone</div>
    <div class="field">Email</div>
    <div class="field tall">Message</div>
    <span class="btn-send">Send</span>
  </div>
  <div class="abs divider"></div>
  <div class="abs info">
    <h3>Contact Info</h3>
    <div class="info-row">
      <svg viewBox="0 0 24 24"><path fill="#1f3a64" d="M12 2a7 7 0 0 0-7 7c0 5 7 13 7 13s7-8 7-13a7 7 0 0 0-7-7zm0 9.5A2.5 2.5 0 1 1 12 6.5a2.5 2.5 0 0 1 0 5z"/></svg>
      <div><b>Larkfield Builders LLC</b>48 Orchard Hill Road, Suite 2<br>Ridgeview, NJ 07400</div>
    </div>
    <div class="info-row">
      <svg viewBox="0 0 24 24"><path fill="#1f3a64" d="M6.6 10.8a15 15 0 0 0 6.6 6.6l2.2-2.2a1 1 0 0 1 1-.25 11.4 11.4 0 0 0 3.6.57 1 1 0 0 1 1 1V20a1 1 0 0 1-1 1A17 17 0 0 1 3 4a1 1 0 0 1 1-1h3.5a1 1 0 0 1 1 1c0 1.25.2 2.45.57 3.6a1 1 0 0 1-.25 1z"/></svg>
      <div><b>Phone</b>201-555-0148</div>
    </div>
    <div class="info-row">
      <svg viewBox="0 0 24 24"><rect x="4" y="8" width="16" height="11" rx="1" fill="#1f3a64"/><rect x="7" y="3" width="10" height="6" fill="none" stroke="#1f3a64" stroke-width="2"/></svg>
      <div><b>Fax</b>201-555-0149</div>
    </div>
    <div class="info-row">
      <svg viewBox="0 0 24 24"><rect x="3" y="5" width="18" height="14" rx="1" fill="#1f3a64"/><path d="m3 6 9 7 9-7" fill="none" stroke="#fff" stroke-width="1.5"/></svg>
      <div><b>Email</b>hello@larkfieldbuilders.example</div>
    </div>
    <div class="follow">Follow Us : <i></i><i></i></div>
  </div>
</section>

<footer>
  <div class="abs footer-line"></div>
  <div class="abs footer-top"></div>
  <nav class="abs footer-nav"><span>Home</span><span>About Us</span><span>Services</span><span>Gallery</span><span>Contact Us</span></nav>
  <div class="abs copyright">© 2017 Larkfield Builders LLC. All rights reserved.</div>
</footer>

</body>
</html>
```